Tilvex Business Card

I have a business that is called "Tilvex Electrical Products LTD" My company deals with top of the range laptops and mobile phones that are exclusive. I need a business card that will be eye catching but not over complicated.

Target Market(s)

Adults aged 19 to 50
Upper middle class

Industry/Entity Type

Business

Requirements
Must have
• Company name/logo (file attached)
• It must have my contact information which is:

• Name: Dale Marwick

• Position: Managing Director 

• Business Address: 7 Hapton Row, London, W4 9QD

• Contact Number: 02085193604
• Mobile: 07814260537
• Email: info@tilvex-goods.co.uk
Nice to have
• Simple and stylish
• Eye catching

```html
<!DOCTYPE html>
<html lang="en">
<head>
<meta charset="utf-8">
<title>Tilvex Electrical Products – Business Card</title>
<link rel="stylesheet" href="https://fonts.googleapis.com/css2?family=Arimo:wght@400&display=swap">
<style>
  :root {
    --card-top: #d6fbe9;
    --card-mid: #ffffff;
    --card-bottom: #d2f6f3;
    --brand-teal: #2bbfd3;
    --tagline-blue: #0a1ee6;
    --name-blue: #0a1ee6;
    --detail-grey: #8e9090;
  }
  * { margin: 0; padding: 0; box-sizing: border-box; }
  html, body {
    width: 1200px;
    height: 783px;
    overflow: hidden;
  }
  body {
    font-family: "Arimo", Arial, sans-serif;
  }
  .business-card {
    position: relative;
    width: 1200px;
    height: 783px;
    background: linear-gradient(180deg, var(--card-top) 0%, var(--card-mid) 42%, var(--card-mid) 60%, var(--card-bottom) 100%);
    overflow: hidden;
  }
  .brand-name {
    position: absolute;
    left: 80px;
    top: 59px;
    font-size: 195px;
    font-weight: 400;
    line-height: 1;
    color: var(--brand-teal);
  }
  .brand-tagline {
    position: absolute;
    left: 84px;
    top: 247px;
    font-size: 51px;
    font-weight: 400;
    line-height: 1;
    letter-spacing: 0.235em;
    color: var(--tagline-blue);
    white-space: nowrap;
  }
  .contact-person {
    position: absolute;
    left: 90px;
    top: 412px;
  }
  .person-name {
    font-size: 33px;
    font-weight: 400;
    line-height: 1;
    letter-spacing: 0.02em;
    color: var(--name-blue);
  }
  .contact-details {
    margin-top: 32px;
    list-style: none;
    font-size: 34px;
    line-height: 36.4px;
    letter-spacing: 0.03em;
    color: var(--detail-grey);
    white-space: nowrap;
  }
</style>
</head>
<body>
  <main class="business-card">
    <h1 class="brand-name">TILVEX</h1>
    <p class="brand-tagline">Electrical Products</p>

    <section class="contact-person">
      <h2 class="person-name">Dale Marwick</h2>
      <ul class="contact-details">
        <li class="job-title">Managing Director</li>
        <li class="address-line">7 Hapton Row</li>
        <li class="address-line">London W4 9QD</li>
        <li class="phone">P: +44 20 8519 3604</li>
        <li class="mobile">M: +44 7814 260 537</li>
        <li class="email">E: info@tilvex-goods.co.uk</li>
      </ul>
    </section>
  </main>
</body>
</html>
```